Global Yoga Apparel Brand Needs a Beautiful Website

We need a website design for a new Yoga brand called Vessa. We develop beautiful, stylish, sexy, comfortable yoga leggings, tops, and yoga apparel for women looking to feel their best, look their best and perform their best on and off the yoga mat.
This will go up at http://vessa.example/ (which is a landing page right now).
We would like to see simple and clean design where the focus will be on powerful images and clean background space. We will be using Shopify to start building on and here are three sites that we would love to see options based off of the look, layout and feel while making something unique at the same time:
1. Tumo.ca
2. marikoven.com
3. www.q-plume.com
The final design should look clean, beautiful, inspiring, powerful and empowering.
Target Market(s)
mostly Females 21-35 range but will be appealing to women over 35 as well.

```html
<!DOCTYPE html>
<html lang="en">
<head>
<meta charset="utf-8">
<title>Vessa — Yoga Apparel for Women</title>
<link rel="stylesheet" href="https://fonts.googleapis.com/css2?family=Oswald:wght@300;400&family=Roboto:wght@300;400;500&display=swap">
<style>
:root{
  --ink:#222;
  --muted:#666;
  --nav:#2a2a2a;
  --footer:#262626;
  --sand:#f1ddb9;
  --sand-deep:#d9b98a;
  --mist:#ebebeb;
  --line:#d8d8d8;
  --teal:#2aa3ad;
  --white:#fff;
  --photo-skin:#c9a98c;
  --photo-grey:#b9b9b9;
}
*{box-sizing:border-box;margin:0;padding:0}
html,body{width:1200px;height:4639px;overflow:hidden;background:var(--white)}
body{position:relative;font-family:"Roboto",Arial,sans-serif;color:var(--ink)}
.abs{position:absolute}
.photo{position:absolute}
.btn{position:absolute;border:2px solid var(--ink);background:var(--white);font:500 13px "Roboto",sans-serif;letter-spacing:1px;text-transform:uppercase;display:flex;align-items:center;justify-content:center;color:var(--ink)}
.display{font-family:"Oswald",sans-serif;font-weight:300;text-transform:uppercase;color:var(--ink)}
.lorem{font-size:14px;color:var(--muted);line-height:1.6}

/* nav */
.site-nav{top:0;left:0;width:1200px;height:56px;background:var(--nav);color:var(--white)}
.site-nav .menu{left:24px;top:20px;font-size:12px;font-weight:500;letter-spacing:.5px;display:flex;gap:22px}
.brand{font:400 22px "Roboto",sans-serif;color:var(--white);letter-spacing:1px}
.site-nav .brand{left:50%;transform:translateX(-50%);top:14px}
.site-nav .tools{right:24px;top:18px;display:flex;gap:22px;align-items:center;font-size:12px}

/* hero */
.hero{top:56px;left:0;width:1200px;height:541px;background:var(--sand)}
.hero-frame{left:470px;top:170px;width:660px;height:310px;border:2px solid var(--sand-deep)}
.hero-title{left:650px;top:210px;font:300 64px "Roboto",sans-serif;color:var(--teal)}
.hero-sub{left:665px;top:312px;width:320px;text-align:center;font-size:16px;color:#444;line-height:1.5}
.hero .btn{left:730px;top:392px;width:188px;height:40px;background:transparent;border-color:#555}

/* leggings band */
.band{left:0;width:1200px;background:var(--mist)}
.leggings{top:597px;height:470px}
.leggings .display{left:74px;top:130px;font-size:40px}
.leggings .lorem{left:74px;top:220px}
.leggings .btn{left:74px;top:280px;width:124px;height:44px}

/* what's new */
.section-title{left:0;width:1200px;text-align:center;font-size:20px}
.section-title span{border-top:2px solid var(--ink);border-bottom:2px solid var(--ink);padding:4px 8px}
.product{position:absolute;width:213px;text-align:center}
.product .thumb{width:213px;height:266px;background:#dcdcdc;position:relative}
.product .thumb i{position:absolute;left:70px;top:20px;width:73px;height:236px;background:#4a4a4a;border-radius:30px 30px 6px 6px}
.product .name{margin-top:40px;font-size:14px;color:var(--muted)}
.product .price{margin-top:28px;font-size:14px;color:var(--muted)}
.rule{left:0;width:1200px;height:1px;background:var(--line)}

/* apparel */
.apparel-title{left:433px;top:2200px;width:365px;text-align:center;font-size:38px;line-height:1.2}

/* cards */
.card-title{position:absolute;width:482px;text-align:center;font-size:20px}
.card-text{position:absolute;width:482px;text-align:center;font-size:13px;color:var(--muted);line-height:1.6}

/* tops */
.tops{top:3161px;height:473px}

/* promo */
.promo-badge{left:574px;top:3755px;width:246px;height:246px;border-radius:50%;background:#111;color:var(--white);text-align:center;font-family:"Oswald",sans-serif}

/* signup */
.signup-head{position:absolute;width:400px;text-align:center;font-size:20px}
.signup-sub{position:absolute;width:400px;text-align:center;font-size:16px;color:#444}
.field{position:absolute;height:36px;border:1px solid #bbb;font-size:12px;color:#999;padding:10px}

/* footer */
.site-footer{left:0;top:4361px;width:1200px;height:278px;background:var(--footer);color:#ddd}
.site-footer h4{font-size:13px;font-weight:500;letter-spacing:1px;color:var(--white);text-transform:uppercase;margin-bottom:16px}
.site-footer ul{list-style:none;font-size:12px;line-height:24px;text-transform:uppercase;color:#bbb}
.socials{display:flex;gap:12px}
.socials span{width:22px;height:22px;border-radius:50%;background:#bbb;display:block}
.legal{left:24px;top:4600px;font-size:12px;color:#bbb;display:flex;gap:26px}
.footer-rule{left:0;top:4584px;width:1200px;height:1px;background:#444}
</style>
</head>
<body>

<header class="abs site-nav">
  <nav class="abs menu"><span>WOMEN</span><span>INSPIRATION</span></nav>
  <div class="abs brand">Vessa</div>
  <div class="abs tools">
    <span>LOGIN</span>
    <svg width="20" height="18" viewBox="0 0 20 18"><path d="M1 2h3l2 10h11l2-7H5" fill="none" stroke="#fff" stroke-width="1.6"/><circle cx="8" cy="16" r="1.5" fill="#fff"/><circle cx="16" cy="16" r="1.5" fill="#fff"/></svg>
    <svg width="16" height="16" viewBox="0 0 16 16"><circle cx="6.5" cy="6.5" r="5" fill="none" stroke="#fff" stroke-width="1.6"/><path d="M10 10l5 5" stroke="#fff" stroke-width="1.6"/></svg>
  </div>
</header>

<section class="abs hero">
  <div class="photo" role="img" aria-label="Woman in teal sports bra and black leggings sitting cross-legged" style="left:80px;top:0;width:440px;height:541px;background:linear-gradient(180deg,#e7cfae,#3a3a3a 80%,#e9d3b0)"></div>
  <div class="abs hero-frame"></div>
  <h1 class="abs hero-title">The Line Up</h1>
  <p class="abs hero-sub">Meet our new selection of leggings<br>you need right now.</p>
  <div class="btn">Shop new leggings</div>
</section>

<section class="abs band leggings">
  <div class="photo" role="img" aria-label="Woman holding an arm-balance yoga pose in black leggings" style="left:390px;top:0;width:730px;height:470px;background:linear-gradient(90deg,#ebebeb,#8a8a8a 45%,#cfcfcf 80%,#ebebeb)"></div>
  <h2 class="abs display">Yoga Leggings</h2>
  <p class="abs lorem">Lorem ipsum dolor sit amet, consectetur adipiscing elit.</p>
  <div class="btn">Shop now</div>
</section>

<h2 class="abs display section-title" style="top:1145px"><span>What's New</span></h2>

<div class="product" style="left:93px;top:1228px"><div class="thumb" role="img" aria-label="Grey leggings"><i></i></div><p class="name">Products Name</p><p class="price">$228.00 USD</p></div>
<div class="product" style="left:359px;top:1228px"><div class="thumb" role="img" aria-label="Model in black tank top"><i style="background:#2e2e2e"></i></div><p class="name">Products Name</p><p class="price">$228.00 USD</p></div>
<div class="product" style="left:625px;top:1228px"><div class="thumb" role="img" aria-label="Grey cropped leggings"><i style="height:170px"></i></div><p class="name">Products Name</p><p class="price">$228.00 USD</p></div>
<div class="product" style="left:889px;top:1228px"><div class="thumb" role="img" aria-label="Grey racerback tank"><i style="left:50px;width:113px;background:#555"></i></div><p class="name">Products Name</p><p class="price">$228.00 USD</p></div>

<div class="product" style="left:93px;top:1645px"><div class="thumb" role="img" aria-label="Grey leggings"><i></i></div><p class="name">Products Name</p><p class="price">$228.00 USD</p></div>
<div class="product" style="left:359px;top:1645px"><div class="thumb" role="img" aria-label="Model in black tank top"><i style="background:#2e2e2e"></i></div><p class="name">Products Name</p><p class="price">$228.00 USD</p></div>
<div class="product" style="left:625px;top:1645px"><div class="thumb" role="img" aria-label="Grey cropped leggings"><i style="height:170px"></i></div><p class="name">Products Name</p><p class="price">$228.00 USD</p></div>
<div class="product" style="left:889px;top:1645px"><div class="thumb" role="img" aria-label="Grey racerback tank"><i style="left:50px;width:113px;background:#555"></i></div><p class="name">Products Name</p><p class="price">$228.00 USD</p></div>

<div class="abs rule" style="top:2078px"></div>

<div class="photo" role="img" aria-label="Woman in camel pose wearing grey top and purple leggings" style="left:0;top:2091px;width:433px;height:445px;background:linear-gradient(180deg,#f4f4f4,#9a9a9a 50%,#3b2a4a 85%,#f2f2f2)"></div>
<h2 class="abs display apparel-title">Yoga Apparel for<br>Women</h2>
<p class="abs lorem" style="left:433px;top:2320px;width:365px;text-align:center">Lorem ipsum dolor sit amet, consectetur adipiscing elit.</p>
<div class="btn" style="left:553px;top:2386px;width:124px;height:40px">Shop now</div>
<div class="photo" role="img" aria-label="Woman in pigeon pose wearing grey top and purple leggings" style="left:798px;top:2091px;width:402px;height:445px;background:linear-gradient(180deg,#f4f4f4,#b0a8a0 45%,#4a2f5e 85%,#f2f2f2)"></div>

<div class="abs rule" style="top:2552px"></div>

<div class="photo" role="img" aria-label="Woman stretching on a blue yoga mat in a red sports bra" style="left:93px;top:2626px;width:482px;height:266px;background:linear-gradient(180deg,#eae7e2,#c6a594 55%,#5f7d9e)"></div>
<div class="photo" role="img" aria-label="Woman lying on her back smiling, with a save up to 70% headline" style="left:625px;top:2626px;width:482px;height:266px;background:linear-gradient(180deg,#e9e6e3,#cdb5a5 60%,#d8d2cc)">
  <div class="display" style="position:absolute;left:190px;top:14px;font-size:36px;font-weight:400;line-height:1">SAVE <span style="font-size:18px">UP TO</span><br><span style="font-size:72px">70%</span></div>
</div>
<h3 class="card-title" style="left:93px;top:2930px;font-weight:400">Our Best Sellers</h3>
<p class="card-text" style="left:93px;top:2970px">Lorem ipsum dolor sit amet, consectetur adipiscing elit, sed do eiusmod tempor incididunt ut labore et dolore magna aliqua.</p>
<div class="btn" style="left:283px;top:3030px;width:102px;height:32px;font-size:11px">Shop now</div>
<h3 class="card-title" style="left:625px;top:2930px;font-weight:400">Save Up To 70%</h3>
<p class="card-text" style="left:625px;top:2970px">Lorem ipsum dolor sit amet, consectetur adipiscing elit, sed do eiusmod tempor incididunt ut labore et dolore magna aliqua.</p>
<div class="btn" style="left:815px;top:3030px;width:102px;height:32px;font-size:11px">Shop now</div>
<div class="abs" style="left:600px;top:2626px;width:1px;height:461px;background:var(--line)"></div>
<div class="abs rule" style="top:3087px;left:93px;width:1014px"></div>

<section class="abs band tops">
  <div class="photo" role="img" aria-label="Woman looking upward in a white sports bra" style="left:278px;top:0;width:433px;height:473px;background:linear-gradient(180deg,#d9d9d9,#b88f6c 40%,#f2f2f2 75%,#c49a78)"></div>
  <h2 class="abs display" style="right:71px;top:150px;font-size:40px">Tops</h2>
  <p class="abs lorem" style="right:71px;top:225px">Lorem ipsum dolor sit amet, consectetur adipiscing elit.</p>
  <div class="btn" style="left:1005px;top:282px;width:124px;height:44px">Shop now</div>
</section>

<div class="photo" role="img" aria-label="Woman in a side-angle yoga pose in a bright studio" style="left:74px;top:3705px;width:461px;height:347px;background:linear-gradient(135deg,#f1f3f3,#9aa8aa 50%,#dfe4e4)"></div>
<div class="photo" role="img" aria-label="Grey leggings shown on a model against a grey wall" style="left:554px;top:3705px;width:575px;height:347px;background:linear-gradient(90deg,#b5bcbc,#8f9898 60%,#b7bdbd)"></div>
<div class="abs promo-badge">
  <div style="font-size:58px;line-height:1;margin-top:36px;font-weight:400">SAVE</div>
  <div style="font-size:110px;line-height:1;font-weight:400">10%</div>
</div>
<div class="abs" style="left:640px;top:3975px;font:500 20px/1.05 'Roboto',sans-serif">On Your<br>First Purchase</div>
<div class="btn" style="left:790px;top:3988px;width:124px;height:40px;background:transparent">Shop now</div>

<h3 class="signup-head display" style="left:200px;top:4130px"><span style="border-top:2px solid var(--ink);border-bottom:2px solid var(--ink);padding:3px 8px">Locations</span></h3>
<p class="signup-sub" style="left:200px;top:4188px">I'm looking for stores and ambassadors near me.</p>
<div class="field" style="left:155px;top:4252px;width:180px">Zip Code</div>
<div class="btn" style="left:350px;top:4252px;width:160px;height:36px;font-size:11px">Search Location</div>
<h3 class="signup-head display" style="left:600px;top:4130px"><span style="border-top:2px solid var(--ink);border-bottom:2px solid var(--ink);padding:3px 8px">Be the First to Know</span></h3>
<p class="signup-sub" style="left:600px;top:4188px">Subscribe For Up To 90% Off Daily!</p>
<div class="field" style="left:695px;top:4252px;width:230px">Enter Your Email Address</div>
<div class="btn" style="left:935px;top:4252px;width:110px;height:36px;font-size:11px">Sign me up</div>

<footer class="abs site-footer">
  <div class="abs brand" style="left:74px;top:42px">Vessa</div>
  <div class="abs" style="left:260px;top:44px"><h4>Follow Us</h4><div class="socials"><span></span><span></span><span></span><span></span><span></span></div></div>
  <div class="abs" style="left:498px;top:44px"><h4>My Account</h4><ul><li>Sign In</li><li>Register</li><li>Order Status</li><li>Returns</li></ul></div>
  <div class="abs" style="left:674px;top:44px"><h4>Contact Us</h4><ul><li>Live Chat</li><li>1.800.555.0142</li></ul></div>
  <div class="abs" style="left:841px;top:44px"><h4>Help</h4><ul><li>Ordering</li><li>Shipping</li><li>Returns</li><li>Sizing</li><li>Our Products</li></ul></div>
  <div class="abs" style="left:1024px;top:44px"><h4>About Us</h4><ul><li>Our Story</li><li>Media</li><li>Investors</li><li>Strategic Sales</li></ul></div>
</footer>
<div class="abs footer-rule"></div>
<div class="abs legal"><span>© 2014 Vessa.</span><span>Privacy Policy</span><span>Terms of Use</span></div>

</body>
</html>
```